diamondscoutline.com - Social Media Branding

diamondscoutline.com --> Social Media Re-Branding & Graphics
Facebook: @dmndscoutline - Instagram: @diamondscoutline - Twitter: @dmndscoutline

Looking to find a good designer to help with my diamondscoutline.com social media sites!
- facebook banner
- twitter banner
- instagram template (square and banner size)
- Quote or Information Template
- Committed Template (uniformed) - see the ones I made (& i am no professional) at diamondscoutline.com/committed - needs to have diamondscoutline.com logo, room for: the committed school and the team the player plays on.

Also willing to pay extra for a graphic that is the "complete package" that detail all of the steps of the recruiting process detailed in diamondscoutline.com

Font styles to use
Sans Serif

Colors
ec1f27
fbee3e

```html
<!DOCTYPE html>
<html lang="en">
<head>
<meta charset="utf-8">
<title>diamondscoutline.com — Free Recruiting Seminar</title>
<link href="https://fonts.googleapis.com/css2?family=Roboto:wght@400;500;700&display=swap" rel="stylesheet">
<style>
  :root {
    --brand-red: #ec1f27;
    --brand-red-deep: #d9161e;
    --brand-yellow: #fbee3e;
    --ball-light: #f4f76a;
    --ball-mid: #c9dc1e;
    --ball-dark: #7e9a0c;
    --white: #ffffff;
  }
  html, body {
    margin: 0;
    padding: 0;
    width: 1200px;
    height: 676px;
    overflow: hidden;
    background: var(--white);
  }
  .banner {
    position: relative;
    width: 1200px;
    height: 676px;
    overflow: hidden;
    background: var(--brand-red);
    font-family: "Roboto", Arial, sans-serif;
    color: var(--white);
  }
  .backdrop {
    position: absolute;
    inset: 0;
    width: 1200px;
    height: 676px;
  }
  .brand {
    position: absolute;
    left: 56px;
    top: 118px;
    display: flex;
    align-items: center;
    gap: 14px;
  }
  .brand-dot {
    width: 64px;
    height: 64px;
    border-radius: 50%;
    background: var(--brand-yellow);
    flex: none;
  }
  .brand-name {
    font-weight: 700;
    font-size: 28px;
    line-height: 1;
    color: var(--white);
    padding-bottom: 8px;
    border-bottom: 2px solid var(--white);
  }
  .seminar-title {
    position: absolute;
    left: 76px;
    top: 218px;
    margin: 0;
    font-weight: 700;
    font-size: 44px;
    line-height: 1.1;
  }
  .seminar-audience {
    position: absolute;
    left: 78px;
    top: 340px;
    margin: 0;
    font-weight: 400;
    font-size: 22px;
  }
  .softball {
    position: absolute;
    left: 420px;
    top: 117px;
    width: 404px;
    height: 404px;
    border-radius: 50%;
    background: radial-gradient(circle at 38% 30%, var(--ball-light) 0%, var(--ball-mid) 55%, var(--ball-dark) 100%);
    box-shadow: 0 18px 30px rgba(0,0,0,0.25);
  }
  .schedule {
    position: absolute;
    left: 860px;
    top: 218px;
    margin: 0;
    font-weight: 700;
    font-size: 44px;
    line-height: 1.1;
  }
  .social-links {
    position: absolute;
    left: 866px;
    top: 346px;
    display: flex;
    gap: 16px;
  }
  .social-links span {
    width: 46px;
    height: 46px;
    border-radius: 50%;
    background: var(--white);
    display: block;
  }
</style>
</head>
<body>
  <main class="banner">
    <svg class="backdrop" viewBox="0 0 1200 676" aria-hidden="true">
      <path d="M0 430 C 220 470, 420 520, 640 500 C 860 480, 1020 420, 1200 405 L1200 676 L0 676 Z" fill="#ffffff"/>
      <path d="M0 452 C 220 492, 420 540, 640 520 C 860 500, 1020 440, 1200 428 L1200 676 L0 676 Z" fill="var(--brand-yellow)"/>
      <circle cx="62" cy="58" r="14" fill="none" stroke="var(--brand-yellow)" stroke-width="2.5"/>
      <line x1="76" y1="62" x2="130" y2="80" stroke="var(--brand-yellow)" stroke-width="2.5"/>
      <circle cx="1032" cy="114" r="14" fill="none" stroke="var(--brand-yellow)" stroke-width="2.5"/>
      <line x1="1042" y1="104" x2="1140" y2="10" stroke="var(--brand-yellow)" stroke-width="2.5"/>
    </svg>

    <div class="brand">
      <span class="brand-dot"></span>
      <span class="brand-name">diamondscoutline.com</span>
    </div>

    <h1 class="seminar-title">Free Recruiting<br>Seminar</h1>
    <p class="seminar-audience">Player, Parents &amp; Coaches</p>

    <div class="softball" role="img" aria-label="Yellow softball with red stitching"></div>

    <p class="schedule">Wednesday<br>7 PM ET</p>
    <div class="social-links" aria-label="Social channels">
      <span></span><span></span><span></span>
    </div>
  </main>
</body>
</html>
```